Aerospace Center needs app design

We need a design that would be a creative and innovative look of a simple idea connecting air traffic control situations with sonification.
We would like to see designs that use the elements shown in the short video which are different pads, showing 4 different colors, connecting with a degree and feeling of urgency. The different pads will be movable over screen, similar as to a whiteboard where you can move things around. Each of those pads has 4 different elements that are shown:
- ATC Event (you can chose different setups)
- Select a status (you can chose between Information, Caution and Alert. Color needs to feel more alert from Information to Alert.
- Notes box (you can open the box and write additional text on it)
- Music (you can chose different files. on the right side you can see a small group of notes. When you hover over the notes, music will be played without pressing a play or stop button.
The second video is an overview of music archival program that is connected with the pads.
Look and feel
Each slider illustrates characteristics of the customer's brand and the style your logo design should communicate.

```html
<!DOCTYPE html>
<html lang="en">
<head>
<meta charset="utf-8">
<title>Soundboards</title>
<link rel="stylesheet" href="https://fonts.googleapis.com/css2?family=Inter:wght@400;500;600;700&display=swap">
<style>
:root{
  --bg:#e9ebf2;
  --sidebar:#0b4bc1;
  --white:#ffffff;
  --ink:#1b1c22;
  --muted:#3c3f48;
  --soft:#8b8f9c;
  --field:#f0f1f6;
  --search:#f3f4f8;
  --green:#2ac769;
  --green-dark:#159a4b;
  --yellow:#fbd500;
  --yellow-dark:#d9b600;
  --red:#f70f0f;
  --red-dark:#c80000;
  --dark:#262626;
  --dark-close:#8d8d8d;
}
*{box-sizing:border-box;margin:0;padding:0}
html,body{width:1200px;height:1091px;overflow:hidden}
body{font-family:"Inter",sans-serif;background:var(--bg);position:relative;color:var(--ink)}

.sidebar{position:absolute;left:0;top:0;width:48px;height:1091px;background:var(--sidebar)}
.brand{position:absolute;top:10px;left:0;width:48px;text-align:center;color:var(--white);font-size:9px;font-weight:700}
.brand-dot{display:block;width:14px;height:14px;border-radius:50%;background:var(--white);margin:0 auto 5px}
.nav-icon{position:absolute;left:13px;width:22px;height:22px}
.nav-notch{position:absolute;left:43px;top:119px;width:0;height:0;border-top:5px solid transparent;border-bottom:5px solid transparent;border-right:6px solid var(--bg)}

.topbar{position:absolute;left:48px;top:0;width:1152px;height:48px;background:var(--white)}
.menu-btn{position:absolute;left:8px;top:9px;width:30px;height:30px;border-radius:50%;background:var(--search)}
.page-title{position:absolute;left:55px;top:14px;font-size:14px;font-weight:600}
.search{position:absolute;left:178px;top:10px;width:662px;height:28px;background:var(--search);border-radius:3px;font-size:8px;color:var(--soft);padding:10px 0 0 30px}
.search svg{position:absolute;left:12px;top:9px}
.round-btn{position:absolute;top:9px;width:30px;height:30px;border-radius:50%;background:var(--search)}
.round-btn svg{position:absolute;left:8px;top:8px}
.avatar{position:absolute;left:1005px;top:8px;width:32px;height:32px;border-radius:50%;background:linear-gradient(135deg,#6a4a3a,#c99a78)}
.user{position:absolute;left:1043px;top:12px;font-size:8px;line-height:11px}
.user-role{color:var(--sidebar)}
.user-name{font-weight:600}

.add-pads{position:absolute;left:66px;top:70px;width:105px;height:31px;border-radius:16px;background:var(--sidebar);color:var(--white);font-size:9px;font-weight:600;padding:10px 0 0 33px}
.add-pads .plus{position:absolute;left:5px;top:5px;width:21px;height:21px;border-radius:50%;background:var(--white)}

.zoom{position:absolute;left:1152px;top:75px;width:14px;height:60px;border-radius:3px;background:var(--sidebar)}
.zoom-label{position:absolute;left:1137px;top:92px;font-size:6px;letter-spacing:1.5px;color:var(--sidebar);font-weight:600;writing-mode:vertical-rl;transform:rotate(180deg)}

.pad{position:absolute;width:190px;background:var(--white);box-shadow:0 20px 40px rgba(40,50,80,.12)}
.pad--green{--accent:var(--green);--accent-deep:var(--green-dark)}
.pad--yellow{--accent:var(--yellow);--accent-deep:var(--yellow-dark)}
.pad--red{--accent:var(--red);--accent-deep:var(--red-dark)}
.pad--dark{--accent:var(--dark);--accent-deep:var(--dark-close)}
.pad-head{height:34px;background:var(--accent);color:var(--white);font-size:11.5px;font-weight:500;position:relative;padding:10px 0 0 46px}
.pad-head .pin{position:absolute;left:20px;top:10px}
.pad-head .close{position:absolute;right:10px;top:11px;width:12px;height:12px;border-radius:50%;background:var(--accent-deep)}
.pad--dark .pad-head .close{background:#d9d9d9}
.pad-body{padding:15px 10px 0 12px}
.field-label{font-size:7.5px;color:var(--muted);height:12px}
.field{height:35px;background:var(--field);margin:4px 0 14px;position:relative;font-size:10px;font-weight:500;padding:12px 0 0 36px}
.field--notes{margin-top:-8px}
.field .ficon{position:absolute;left:11px;top:9px}
.field .chev{position:absolute;right:12px;top:15px}
.notes-open{height:101px}
.notes-text{font-size:8.5px;font-weight:400;color:var(--muted);line-height:14px;padding:20px 10px 0 0;margin-left:-26px}
.pad-foot{position:relative;height:43px}
.pad-foot svg.wave{position:absolute;left:0;bottom:0}
.play{position:absolute;left:73px;bottom:-13px;width:44px;height:44px;border-radius:50%;background:var(--accent)}
.play svg{position:absolute;left:11px;top:11px}
</style>
</head>
<body>

<aside class="sidebar">
  <div class="brand"><span class="brand-dot"></span>SKY</div>
  <svg class="nav-icon" style="top:111px" viewBox="0 0 22 22" fill="none" stroke="#fff" stroke-width="1.4"><rect x="2" y="2" width="18" height="18" rx="1"/><path d="M2 7h18M6 10v7M11 10v7M16 10v7"/><circle cx="6" cy="13" r="1.3"/><circle cx="11" cy="15" r="1.3"/><circle cx="16" cy="12" r="1.3"/></svg>
  <span class="nav-notch"></span>
  <svg class="nav-icon" style="top:151px" viewBox="0 0 22 22" fill="none" stroke="#fff" stroke-width="1.6"><rect x="2" y="2" width="7" height="8"/><rect x="12" y="2" width="8" height="6"/><rect x="2" y="13" width="7" height="7"/><rect x="12" y="11" width="8" height="9"/></svg>
  <svg class="nav-icon" style="top:197px" viewBox="0 0 22 22" fill="none" stroke="#fff" stroke-width="1.4"><rect x="11" y="2" width="9" height="7" rx="1"/><path d="M13 5l2 2 3-3"/><circle cx="7" cy="10" r="3"/><path d="M2 20v-3a5 5 0 0 1 10 0v3"/></svg>
  <svg class="nav-icon" style="top:244px" viewBox="0 0 22 22" fill="none" stroke="#fff" stroke-width="1.4"><rect x="6" y="2" width="14" height="10" rx="1"/><path d="M9 6h8M9 9h6"/><path d="M4 7H2v9h3v4l4-4h7v-2"/></svg>
  <svg class="nav-icon" style="top:286px" viewBox="0 0 22 22" fill="none" stroke="#fff" stroke-width="1.6"><path d="M6 18V4l10 3M6 10l10-3"/><circle cx="4" cy="18" r="2.5"/><path d="M12 14h8M12 18h8"/></svg>
  <svg class="nav-icon" style="top:980px" viewBox="0 0 22 22" fill="none" stroke="#fff" stroke-width="1.6"><path d="M13 4H4v14l5 2V6l-5-2"/><path d="M13 18v-4M14 11h7M18 8l3 3-3 3"/></svg>
</aside>

<header class="topbar">
  <div class="menu-btn"><svg width="30" height="30" viewBox="0 0 30 30" stroke="#333" stroke-width="1.4"><path d="M9 11h12M9 15h12M9 19h12"/></svg></div>
  <div class="page-title">Soundboards</div>
  <div class="search"><svg width="10" height="10" viewBox="0 0 10 10" fill="none" stroke="#333" stroke-width="1.2"><circle cx="4.3" cy="4.3" r="3.3"/><path d="M6.8 6.8L9.3 9.3"/></svg>Type your text here...</div>
  <div class="round-btn" style="left:924px"><svg width="14" height="14" viewBox="0 0 14 14" fill="none" stroke="#333" stroke-width="1.2"><rect x="1" y="3" width="12" height="9" rx="2"/><path d="M1.5 4l5.5 4 5.5-4"/></svg></div>
  <div class="round-btn" style="left:962px"><svg width="14" height="14" viewBox="0 0 14 14" fill="none" stroke="#333" stroke-width="1.2"><path d="M3 10V6a4 4 0 0 1 6-3.5M11 7v3M2 10h10M6 12h2"/><circle cx="11" cy="3.5" r="2" fill="#0b4bc1" stroke="none"/></svg></div>
  <div class="avatar" role="img" aria-label="User profile photo"></div>
  <div class="user"><div class="user-role">Admin</div><div class="user-name">Lena Hartwell</div></div>
  <div class="round-btn" style="left:1115px"><svg width="14" height="14" viewBox="0 0 14 14" fill="none" stroke="#333" stroke-width="1.3"><circle cx="7" cy="7" r="2.2"/><path d="M7 1l1.5 1.4 2-.4.6 2 1.9.9-.6 2 .6 2-1.9.9-.6 2-2-.4L7 13l-1.5-1.4-2 .4-.6-2-1.9-.9.6-2-.6-2 1.9-.9.6-2 2 .4z"/></svg></div>
</header>

<div class="add-pads"><span class="plus"><svg width="21" height="21" viewBox="0 0 21 21" stroke="#0b4bc1" stroke-width="2"><path d="M10.5 6v9M6 10.5h9"/></svg></span>Add New Pads</div>

<div class="zoom"><svg width="14" height="60" viewBox="0 0 14 60" fill="#fff"><path d="M4 7l3-3 3 3z"/><rect x="5" y="22" width="4" height="14" rx="2"/><path d="M4 53l3 3 3-3z"/></svg></div>
<div class="zoom-label">ZOOM</div>

<svg width="0" height="0" style="position:absolute">
  <defs>
    <symbol id="i-pin" viewBox="0 0 14 14"><path d="M8 1l5 5-2 1-2 3 .5 2.5L3 7l2.5.5 3-2L8 1zM5 9l-4 4" fill="none" stroke="#fff" stroke-width="1.1"/></symbol>
    <symbol id="i-x" viewBox="0 0 12 12"><path d="M4 4l4 4M8 4l-4 4" stroke="#fff" stroke-width="1.2"/></symbol>
    <symbol id="i-chev" viewBox="0 0 8 5"><path d="M1 1l3 3 3-3" fill="none" stroke="#222" stroke-width="1.3"/></symbol>
    <symbol id="i-event" viewBox="0 0 16 16"><g fill="none" stroke="#b9bcc6" stroke-width="1"><path d="M2 15V8h12v7M5 8V5h6v3M8 5V1M6 2h4"/><circle cx="8" cy="11" r="1.5"/></g></symbol>
    <symbol id="i-status" viewBox="0 0 16 16"><g fill="none" stroke="#b9bcc6" stroke-width="1"><rect x="1" y="2" width="10" height="9"/><rect x="5" y="5" width="10" height="10"/><path d="M10 8v4M10 13v.5"/></g></symbol>
    <symbol id="i-sound" viewBox="0 0 16 16"><g fill="none" stroke="#b9bcc6" stroke-width="1"><rect x="2" y="2" width="12" height="12" rx="2"/><path d="M5 11V8a3 3 0 0 1 6 0v3"/></g></symbol>
    <symbol id="i-notes" viewBox="0 0 16 16"><g fill="none" stroke="#b9bcc6" stroke-width="1"><rect x="1" y="3" width="10" height="12"/><path d="M5 3V1h10v12h-4M3 7h6M3 10h6M3 13h4"/></g></symbol>
    <symbol id="i-music" viewBox="0 0 22 22"><g fill="none" stroke="#fff" stroke-width="1.6"><path d="M6 18V8l7-2v10"/><circle cx="4.5" cy="18" r="2"/><circle cx="11.5" cy="16" r="2"/><path d="M16 3v5M13.5 5.5h5M18 13v5M15.5 15.5h5"/></g></symbol>
  </defs>
</svg>

<!-- Pad template repeated -->
<section class="pad pad--green" style="left:129px;top:133px">
  <div class="pad-head"><svg class="pin" width="14" height="14"><use href="#i-pin"/></svg>Soundboard 1<span class="close"><svg width="12" height="12"><use href="#i-x"/></svg></span></div>
  <div class="pad-body">
    <div class="field-label">Select ATC Event</div>
    <div class="field"><svg class="ficon" width="16" height="16"><use href="#i-event"/></svg>Landing<svg class="chev" width="8" height="5"><use href="#i-chev"/></svg></div>
    <div class="field-label">Select Status Level</div>
    <div class="field"><svg class="ficon" width="16" height="16"><use href="#i-status"/></svg>1.Information<svg class="chev" width="8" height="5"><use href="#i-chev"/></svg></div>
    <div class="field-label">Select Sound File</div>
    <div class="field"><svg class="ficon" width="16" height="16"><use href="#i-sound"/></svg>Batch Tocatta<svg class="chev" width="8" height="5"><use href="#i-chev"/></svg></div>
    <div class="field field--notes"><svg class="ficon" width="16" height="16"><use href="#i-notes"/></svg>Notes<svg class="chev" width="8" height="5"><use href="#i-chev"/></svg></div>
  </div>
  <div class="pad-foot"><svg class="wave" width="190" height="20" viewBox="0 0 190 20"><path d="M0 9Q95 1 190 11" fill="none" stroke="var(--accent)" stroke-opacity=".3"/><path d="M0 12Q95 5 190 14" fill="none" stroke="var(--accent)" stroke-opacity=".5"/><path d="M0 12Q95 8 190 16V20H0z" fill="var(--accent)"/></svg><div class="play"><svg width="22" height="22"><use href="#i-music"/></svg></div></div>
</section>

<section class="pad pad--green" style="left:378px;top:111px">
  <div class="pad-head"><svg class="pin" width="14" height="14"><use href="#i-pin"/></svg>Soundboard 2<span class="close"><svg width="12" height="12"><use href="#i-x"/></svg></span></div>
  <div class="pad-body">
    <div class="field-label">Select ATC Event</div>
    <div class="field"><svg class="ficon" width="16" height="16"><use href="#i-event"/></svg>Landing<svg class="chev" width="8" height="5"><use href="#i-chev"/></svg></div>
    <div class="field-label">Select Status Level</div>
    <div class="field"><svg class="ficon" width="16" height="16"><use href="#i-status"/></svg>1.Information<svg class="chev" width="8" height="5"><use href="#i-chev"/></svg></div>
    <div class="field-label">Select Sound File</div>
    <div class="field"><svg class="ficon" width="16" height="16"><use href="#i-sound"/></svg>Batch Tocatta<svg class="chev" width="8" height="5"><use href="#i-chev"/></svg></div>
    <div class="field field--notes notes-open"><svg class="ficon" width="16" height="16"><use href="#i-notes"/></svg>Notes<svg class="chev" width="8" height="5"><use href="#i-chev"/></svg>
      <p class="notes-text">Sed ut perspiciatis unde omnis iste natus error sit voluptatem accusan-tium doloremque laudantium,</p></div>
  </div>
  <div class="pad-foot" style="height:40px;margin-top:-6px"><svg class="wave" width="190" height="20" viewBox="0 0 190 20"><path d="M0 9Q95 1 190 11" fill="none" stroke="var(--accent)" stroke-opacity=".3"/><path d="M0 12Q95 5 190 14" fill="none" stroke="var(--accent)" stroke-opacity=".5"/><path d="M0 12Q95 8 190 16V20H0z" fill="var(--accent)"/></svg><div class="play"><svg width="22" height="22"><use href="#i-music"/></svg></div></div>
</section>

<section class="pad pad--yellow" style="left:628px;top:133px">
  <div class="pad-head"><svg class="pin" width="14" height="14"><use href="#i-pin"/></svg>Soundboard 3<span class="close"><svg width="12" height="12"><use href="#i-x"/></svg></span></div>
  <div class="pad-body">
    <div class="field-label">Select ATC Event</div>
    <div class="field"><svg class="ficon" width="16" height="16"><use href="#i-event"/></svg>Depature<svg class="chev" width="8" height="5"><use href="#i-chev"/></svg></div>
    <div class="field-label">Select Status Level</div>
    <div class="field"><svg class="ficon" width="16" height="16"><use href="#i-status"/></svg>2.Caution<svg class="chev" width="8" height="5"><use href="#i-chev"/></svg></div>
    <div class="field-label">Select Sound File</div>
    <div class="field"><svg class="ficon" width="16" height="16"><use href="#i-sound"/></svg>Batch Tocatta<svg class="chev" width="8" height="5"><use href="#i-chev"/></svg></div>
    <div class="field field--notes"><svg class="ficon" width="16" height="16"><use href="#i-notes"/></svg>Notes<svg class="chev" width="8" height="5"><use href="#i-chev"/></svg></div>
  </div>
  <div class="pad-foot"><svg class="wave" width="190" height="20" viewBox="0 0 190 20"><path d="M0 9Q95 1 190 11" fill="none" stroke="var(--accent)" stroke-opacity=".3"/><path d="M0 12Q95 5 190 14" fill="none" stroke="var(--accent)" stroke-opacity=".5"/><path d="M0 12Q95 8 190 16V20H0z" fill="var(--accent)"/></svg><div class="play"><svg width="22" height="22"><use href="#i-music"/></svg></div></div>
</section>

<section class="pad pad--red" style="left:888px;top:187px">
  <div class="pad-head"><svg class="pin" width="14" height="14"><use href="#i-pin"/></svg>Soundboard 4<span class="close"><svg width="12" height="12"><use href="#i-x"/></svg></span></div>
  <div class="pad-body">
    <div class="field-label">Select ATC Event</div>
    <div class="field"><svg class="ficon" width="16" height="16"><use href="#i-event"/></svg>Moon<svg class="chev" width="8" height="5"><use href="#i-chev"/></svg></div>
    <div class="field-label">Select Status Level</div>
    <div class="field"><svg class="ficon" width="16" height="16"><use href="#i-status"/></svg>3.Alert<svg class="chev" width="8" height="5"><use href="#i-chev"/></svg></div>
    <div class="field-label">Select Sound File</div>
    <div class="field"><svg class="ficon" width="16" height="16"><use href="#i-sound"/></svg>Batch Tocatta<svg class="chev" width="8" height="5"><use href="#i-chev"/></svg></div>
    <div class="field field--notes"><svg class="ficon" width="16" height="16"><use href="#i-notes"/></svg>Notes<svg class="chev" width="8" height="5"><use href="#i-chev"/></svg></div>
  </div>
  <div class="pad-foot"><svg class="wave" width="190" height="20" viewBox="0 0 190 20"><path d="M0 9Q95 1 190 11" fill="none" stroke="var(--accent)" stroke-opacity=".3"/><path d="M0 12Q95 5 190 14" fill="none" stroke="var(--accent)" stroke-opacity=".5"/><path d="M0 12Q95 8 190 16V20H0z" fill="var(--accent)"/></svg><div class="play"><svg width="22" height="22"><use href="#i-music"/></svg></div></div>
</section>

<section class="pad pad--dark" style="left:129px;top:561px">
  <div class="pad-head"><svg class="pin" width="14" height="14"><use href="#i-pin"/></svg>Soundboard 1<span class="close"><svg width="12" height="12"><use href="#i-x" style="stroke:#262626"/></svg></span></div>
  <div class="pad-body">
    <div class="field-label">Select ATC Event</div>
    <div class="field"><svg class="ficon" width="16" height="16"><use href="#i-event"/></svg>Landing<svg class="chev" width="8" height="5"><use href="#i-chev"/></svg></div>
    <div class="field-label">Select Status Level</div>
    <div class="field"><svg class="ficon" width="16" height="16"><use href="#i-status"/></svg>1.Information<svg class="chev" width="8" height="5"><use href="#i-chev"/></svg></div>
    <div class="field-label">Select Sound File</div>
    <div class="field"><svg class="ficon" width="16" height="16"><use href="#i-sound"/></svg>Batch Tocatta<svg class="chev" width="8" height="5"><use href="#i-chev"/></svg></div>
    <div class="field field--notes"><svg class="ficon" width="16" height="16"><use href="#i-notes"/></svg>Notes<svg class="chev" width="8" height="5"><use href="#i-chev"/></svg></div>
  </div>
  <div class="pad-foot"><svg class="wave" width="190" height="20" viewBox="0 0 190 20"><path d="M0 9Q95 1 190 11" fill="none" stroke="var(--accent)" stroke-opacity=".3"/><path d="M0 12Q95 5 190 14" fill="none" stroke="var(--accent)" stroke-opacity=".5"/><path d="M0 12Q95 8 190 16V20H0z" fill="var(--accent)"/></svg><div class="play"><svg width="22" height="22"><use href="#i-music"/></svg></div></div>
</section>

<section class="pad pad--dark" style="left:415px;top:621px">
  <div class="pad-head"><svg class="pin" width="14" height="14"><use href="#i-pin"/></svg>Soundboard 1<span class="close"></span></div>
  <div class="pad-body">
    <div class="field-label">Select ATC Event</div>
    <div class="field"><svg class="ficon" width="16" height="16"><use href="#i-event"/></svg>Landing<svg class="chev" width="8" height="5"><use href="#i-chev"/></svg></div>
    <div class="field-label">Select Status Level</div>
    <div class="field"><svg class="ficon" width="16" height="16"><use href="#i-status"/></svg>1.Information<svg class="chev" width="8" height="5"><use href="#i-chev"/></svg></div>
    <div class="field-label">Select Sound File</div>
    <div class="field"><svg class="ficon" width="16" height="16"><use href="#i-sound"/></svg>Batch Tocatta<svg class="chev" width="8" height="5"><use href="#i-chev"/></svg></div>
    <div class="field field--notes"><svg class="ficon" width="16" height="16"><use href="#i-notes"/></svg>Notes<svg class="chev" width="8" height="5"><use href="#i-chev"/></svg></div>
  </div>
  <div class="pad-foot"><svg class="wave" width="190" height="20" viewBox="0 0 190 20"><path d="M0 9Q95 1 190 11" fill="none" stroke="var(--accent)" stroke-opacity=".3"/><path d="M0 12Q95 5 190 14" fill="none" stroke="var(--accent)" stroke-opacity=".5"/><path d="M0 12Q95 8 190 16V20H0z" fill="var(--accent)"/></svg><div class="play"><svg width="22" height="22"><use href="#i-music"/></svg></div></div>
</section>

<section class="pad pad--dark" style="left:687px;top:561px">
  <div class="pad-head"><svg class="pin" width="14" height="14"><use href="#i-pin"/></svg>Soundboard 1<span class="close"></span></div>
  <div class="pad-body">
    <div class="field-label">Select ATC Event</div>
    <div class="field"><svg class="ficon" width="16" height="16"><use href="#i-event"/></svg>Landing<svg class="chev" width="8" height="5"><use href="#i-chev"/></svg></div>
    <div class="field-label">Select Status Level</div>
    <div class="field"><svg class="ficon" width="16" height="16"><use href="#i-status"/></svg>1.Information<svg class="chev" width="8" height="5"><use href="#i-chev"/></svg></div>
    <div class="field-label">Select Sound File</div>
    <div class="field"><svg class="ficon" width="16" height="16"><use href="#i-sound"/></svg>Batch Tocatta<svg class="chev" width="8" height="5"><use href="#i-chev"/></svg></div>
    <div class="field field--notes"><svg class="ficon" width="16" height="16"><use href="#i-notes"/></svg>Notes<svg class="chev" width="8" height="5"><use href="#i-chev"/></svg></div>
  </div>
  <div class="pad-foot"><svg class="wave" width="190" height="20" viewBox="0 0 190 20"><path d="M0 9Q95 1 190 11" fill="none" stroke="var(--accent)" stroke-opacity=".3"/><path d="M0 12Q95 5 190 14" fill="none" stroke="var(--accent)" stroke-opacity=".5"/><path d="M0 12Q95 8 190 16V20H0z" fill="var(--accent)"/></svg><div class="play"><svg width="22" height="22"><use href="#i-music"/></svg></div></div>
</section>

<section class="pad pad--dark" style="left:941px;top:603px">
  <div class="pad-head"><svg class="pin" width="14" height="14"><use href="#i-pin"/></svg>Soundboard 1<span class="close"></span></div>
  <div class="pad-body">
    <div class="field-label">Select ATC Event</div>
    <div class="field"><svg class="ficon" width="16" height="16"><use href="#i-event"/></svg>Landing<svg class="chev" width="8" height="5"><use href="#i-chev"/></svg></div>
    <div class="field-label">Select Status Level</div>
    <div class="field"><svg class="ficon" width="16" height="16"><use href="#i-status"/></svg>1.Information<svg class="chev" width="8" height="5"><use href="#i-chev"/></svg></div>
    <div class="field-label">Select Sound File</div>
    <div class="field"><svg class="ficon" width="16" height="16"><use href="#i-sound"/></svg>Batch Tocatta<svg class="chev" width="8" height="5"><use href="#i-chev"/></svg></div>
    <div class="field field--notes"><svg class="ficon" width="16" height="16"><use href="#i-notes"/></svg>Notes<svg class="chev" width="8" height="5"><use href="#i-chev"/></svg></div>
  </div>
  <div class="pad-foot"><svg class="wave" width="190" height="20" viewBox="0 0 190 20"><path d="M0 9Q95 1 190 11" fill="none" stroke="var(--accent)" stroke-opacity=".3"/><path d="M0 12Q95 5 190 14" fill="none" stroke="var(--accent)" stroke-opacity=".5"/><path d="M0 12Q95 8 190 16V20H0z" fill="var(--accent)"/></svg><div class="play"><svg width="22" height="22"><use href="#i-music"/></svg></div></div>
</section>

</body>
</html>
```